MINIMAL Design Alteration for a UI/UX design

- Below is the Sketch file as well the logo for a UI/UX infrustructure for an application that enables users to book instant cleaning services. However when it was started the project enabled users to book a wide variety of services. The logo includes a mop as well as a hammer. We want the designer to do the following two small edits on the platform. Them being :
1. Edit the logo as to include the mop and another symbol of cleaning in a visually appealing manner
2. Modify the UI/UX screen in the sketch file removing the other services and only maintaining the cleaning option in A VISUALLY APPEALING MANNER
Any useful edits would be appreciated !

best

Requirements
Must have
• ABILITY TO BOOK CLEANING SERVICE ONLY IN A APPEALING MANNER

```html
<!DOCTYPE html>
<html lang="en">
<head>
<meta charset="utf-8">
<title>NestSweep — Reservations</title>
<link rel="stylesheet" href="https://fonts.googleapis.com/css2?family=Roboto:wght@300;400;500;700&display=swap">
<style>
  :root {
    --backdrop: #9fd8ef;
    --screen-top: #e6fbff;
    --screen-bottom: #effde6;
    --brand-green: #7dc242;
    --brand-blue: #29a3dc;
    --ink: #1a1a1a;
    --muted: #8a8a8a;
    --line: #e4e4e4;
    --white: #ffffff;
    --dot-pending: #f5a623;
    --dot-confirmed: #2cb84f;
    --tab-grey: #9b9b9b;
    --illustration: #b9c3c9;
  }
  * { box-sizing: border-box; margin: 0; padding: 0; }
  html, body { width: 1200px; height: 1000px; overflow: hidden; }
  body {
    background: linear-gradient(180deg, #b3e2f3 0%, var(--backdrop) 100%);
    font-family: "Roboto", Helvetica, Arial, sans-serif;
    position: relative;
  }
  .screen {
    position: absolute;
    top: 200px;
    width: 338px;
    height: 603px;
    overflow: hidden;
    background: linear-gradient(180deg, var(--screen-top) 0%, var(--screen-bottom) 100%);
    border: 1px solid #c9d3d8;
  }
  .screen--welcome { left: 181px; }
  .screen--list { left: 683px; }

  .status-bar {
    position: absolute; top: 0; left: 0; right: 0; height: 20px;
    display: flex; align-items: center; justify-content: space-between;
    padding: 0 8px; font-size: 10px; color: var(--ink);
  }
  .status-bar .battery { display: flex; align-items: center; gap: 3px; }
  .status-bar .battery i {
    display: inline-block; width: 20px; height: 9px; border: 1px solid var(--ink);
    border-radius: 2px; background: var(--ink); box-shadow: inset 0 0 0 1px var(--white);
  }

  /* welcome */
  .brand { position: absolute; top: 87px; left: 0; right: 0; text-align: center; }
  .brand-mark {
    width: 88px; height: 88px; margin: 0 auto 12px; background: var(--brand-green); border-radius: 12px;
  }
  .brand-name { font-size: 28px; font-weight: 700; color: var(--brand-green); letter-spacing: -0.3px; }
  .welcome-title {
    position: absolute; top: 276px; left: 0; right: 0; text-align: center;
    font-size: 28px; font-weight: 300; line-height: 29px; color: var(--brand-green);
  }
  .welcome-hint {
    position: absolute; top: 396px; left: 0; right: 0; text-align: center;
    font-size: 22px; font-weight: 300; line-height: 25px; color: var(--brand-blue);
  }
  .welcome-hint b { font-weight: 700; }
  .hint-arrow { position: absolute; top: 452px; left: 150px; }

  /* list */
  .search {
    position: absolute; top: 56px; left: 32px; width: 274px; height: 27px;
    background: var(--white); border-radius: 4px; box-shadow: 0 1px 4px rgba(0,0,0,0.08);
    display: flex; align-items: center; justify-content: center; gap: 6px;
    font-size: 12px; color: var(--muted);
  }
  .reservations { position: absolute; top: 125px; left: 0; right: 0; list-style: none; }
  .reservation {
    position: relative; height: 70px; background: var(--white);
    border-bottom: 1px solid var(--line); padding: 9px 0 0 15px;
  }
  .reservation-title { font-size: 13px; font-weight: 500; color: var(--ink); position: relative; padding-left: 17px; }
  .reservation-title::before {
    content: ""; position: absolute; left: 1px; top: 4px; width: 9px; height: 9px; border-radius: 50%;
  }
  .reservation--pending .reservation-title::before { background: var(--dot-pending); }
  .reservation--confirmed .reservation-title::before { background: var(--dot-confirmed); }
  .reservation-time { font-size: 11px; color: var(--brand-blue); margin-top: 3px; }
  .reservation-address { font-size: 10.5px; color: var(--muted); margin-top: 1px; }
  .reservation-art {
    position: absolute; right: 14px; top: 9px; width: 60px; height: 54px;
    background: linear-gradient(160deg, #d3dadf, var(--illustration)); border-radius: 8px;
  }

  /* tab bar */
  .tab-bar {
    position: absolute; left: 0; right: 0; bottom: 0; height: 45px;
    background: #f8f8f8; border-top: 1px solid var(--line);
  }
  .tab {
    position: absolute; top: 8px; width: 60px; text-align: center;
    font-size: 8px; color: var(--tab-grey);
  }
  .tab svg { display: block; margin: 0 auto 3px; }
  .tab--active { color: var(--brand-blue); }
  .tab--reservations { left: 2px; }
  .tab--notifications { left: 64px; }
  .tab--account { left: 214px; }
  .tab--more { left: 268px; }
  .add-button {
    position: absolute; left: 126px; top: 528px; width: 86px; height: 86px; border-radius: 50%;
    background: var(--white); border: 1px solid var(--line);
    display: flex; align-items: flex-start; justify-content: center; padding-top: 28px;
  }
</style>
</head>
<body>

<section class="screen screen--welcome">
  <div class="status-bar"><span>●●●●● Corvio</span><span>9:41 AM</span><span class="battery">100% <i></i></span></div>

  <div class="brand">
    <div class="brand-mark"></div>
    <div class="brand-name">NestSweep</div>
  </div>

  <p class="welcome-title">welcome to<br>NestSweep!</p>
  <p class="welcome-hint">tap <b>+</b> to make your<br>first reservation!</p>

  <svg class="hint-arrow" width="80" height="70" viewBox="0 0 80 70" aria-hidden="true">
    <path d="M66 4 C72 22 62 36 44 38 C30 40 26 50 16 60" fill="none" stroke="#29a3dc" stroke-width="3" stroke-linecap="round"/>
    <path d="M6 52 L14 62 L26 58" fill="none" stroke="#29a3dc" stroke-width="3" stroke-linecap="round" stroke-linejoin="round"/>
  </svg>

  <nav class="tab-bar">
    <div class="tab tab--active tab--reservations">
      <svg width="18" height="16" viewBox="0 0 18 16"><rect x="1" y="2" width="16" height="13" rx="2" fill="#dcdcdc"/><rect x="1" y="2" width="16" height="4" rx="1" fill="#e2513c"/></svg>Reservations</div>
    <div class="tab tab--notifications">
      <svg width="16" height="16" viewBox="0 0 16 16"><path d="M8 1 C4 1 3 5 3 8 L1.5 12 H14.5 L13 8 C13 5 12 1 8 1Z" fill="#f5b400"/><circle cx="8" cy="14" r="1.8" fill="#f5b400"/></svg>Notifications</div>
    <div class="tab tab--account">
      <svg width="16" height="16" viewBox="0 0 16 16"><circle cx="8" cy="5" r="4" fill="#f5a623"/><path d="M1 16 C1 11 15 11 15 16Z" fill="#4a6a86"/></svg>Account</div>
    <div class="tab tab--more">
      <svg width="16" height="16" viewBox="0 0 16 16"><circle cx="8" cy="8" r="7.5" fill="#cfd6db"/><circle cx="4.5" cy="8" r="1.2" fill="#555"/><circle cx="8" cy="8" r="1.2" fill="#555"/><circle cx="11.5" cy="8" r="1.2" fill="#555"/></svg>More</div>
  </nav>
  <div class="add-button"><svg width="24" height="24" viewBox="0 0 24 24"><path d="M12 1V23M1 12H23" stroke="#7a7a7a" stroke-width="2.5"/></svg></div>
</section>

<section class="screen screen--list">
  <div class="status-bar"><span>●●●●● Corvio</span><span>9:41 AM</span><span class="battery">100% <i></i></span></div>

  <div class="search">
    <svg width="11" height="11" viewBox="0 0 11 11"><circle cx="4.5" cy="4.5" r="3.6" fill="none" stroke="#8a8a8a" stroke-width="1.3"/><path d="M7.3 7.3L10.3 10.3" stroke="#8a8a8a" stroke-width="1.3"/></svg>
    Search Reservations
  </div>

  <ul class="reservations">
    <li class="reservation reservation--pending">
      <p class="reservation-title">Cleaning</p>
      <p class="reservation-time">Janurary 1, 2018 at 06:30 PM</p>
      <p class="reservation-address">123 Maple Row Apt. C Riverton</p>
      <div class="reservation-art" role="img" aria-label="Vacuum cleaner illustration"></div>
    </li>
    <li class="reservation reservation--confirmed">
      <p class="reservation-title">Cleaning</p>
      <p class="reservation-time">January 2, 2018 at 08:45 PM</p>
      <p class="reservation-address">526 Willow Bend Apt. 729, Riverton</p>
      <div class="reservation-art" role="img" aria-label="Vacuum cleaner illustration"></div>
    </li>
    <li class="reservation reservation--confirmed">
      <p class="reservation-title">Cleaning</p>
      <p class="reservation-time">January 7, 2018 at 09:00 AM</p>
      <p class="reservation-address">860 Cedar Lane Apt. 204, Riverton</p>
      <div class="reservation-art" role="img" aria-label="Vacuum cleaner illustration"></div>
    </li>
  </ul>

  <nav class="tab-bar">
    <div class="tab tab--active tab--reservations">
      <svg width="18" height="16" viewBox="0 0 18 16"><rect x="1" y="2" width="16" height="13" rx="2" fill="#dcdcdc"/><rect x="1" y="2" width="16" height="4" rx="1" fill="#e2513c"/></svg>Reservations</div>
    <div class="tab tab--notifications">
      <svg width="16" height="16" viewBox="0 0 16 16"><path d="M8 1 C4 1 3 5 3 8 L1.5 12 H14.5 L13 8 C13 5 12 1 8 1Z" fill="#f5b400"/><circle cx="8" cy="14" r="1.8" fill="#f5b400"/></svg>Notifications</div>
    <div class="tab tab--account">
      <svg width="16" height="16" viewBox="0 0 16 16"><circle cx="8" cy="5" r="4" fill="#f5a623"/><path d="M1 16 C1 11 15 11 15 16Z" fill="#4a6a86"/></svg>Account</div>
    <div class="tab tab--more">
      <svg width="16" height="16" viewBox="0 0 16 16"><circle cx="8" cy="8" r="7.5" fill="#cfd6db"/><circle cx="4.5" cy="8" r="1.2" fill="#555"/><circle cx="8" cy="8" r="1.2" fill="#555"/><circle cx="11.5" cy="8" r="1.2" fill="#555"/></svg>More</div>
  </nav>
  <div class="add-button"><svg width="24" height="24" viewBox="0 0 24 24"><path d="M12 1V23M1 12H23" stroke="#7a7a7a" stroke-width="2.5"/></svg></div>
</section>

</body>
</html>
```